yieldcompassplans.com needs a good website design and logo

Our company sells memberships to a website that generates systematic rules-based investment strategies on a monthly basis.
I would like a modern professional wordpress design that uses the color blue. It should communicate financial safety and growth. The company is based in Denver Colorado USA.
Please see current website: https://www.yieldcompassplans.com

Target Market(s)

individual investors looking to improve their investment performance. Looking for improved returns or ways to limit losses.

Industry/Entity Type

Investment

Logo Text

yieldcompassPlans

Coding

Coded - Design and coding required

Font styles to use
Sans Serif

Colors
3176b5
85abd2
0355a3
00a990

Requirements
Must have
• I've included details in the attached document.
• The colors selected below are suggestions. While we want the color blue, please use the best version of blue you think is good.
Nice to have
• The design with work with wordpress. We would like to be able to modify the theme later using elementor and a base theme, like maybe astra?
• There is additional work to be done after this contest including designing other pages.
• The site uses some plotvanery.com to display charts and investment performance, if you have experience making these charts and graphs look good, that would be valuable.

```html
<!DOCTYPE html>
<html lang="en">
<head>
<meta charset="utf-8">
<title>yieldcompassPlans</title>
<link href="https://fonts.googleapis.com/css2?family=Montserrat:wght@400;500;600;700;800&family=Open+Sans:wght@400;600&display=swap" rel="stylesheet">
<style>
:root{
  --navy:#0a3f7e;
  --blue:#0355a3;
  --mid:#3176b5;
  --light:#85abd2;
  --teal:#00a990;
  --teal-dark:#0b8f88;
  --ink:#2a2f36;
  --muted:#8a929c;
  --grey:#eeeff1;
  --white:#ffffff;
}
*{box-sizing:border-box;margin:0;padding:0}
html,body{width:1200px;height:2944px;overflow:hidden}
body{font-family:"Open Sans",Arial,sans-serif;color:var(--ink);background:var(--white);position:relative}
h1,h2,h3,.btn,.nav a,.brand{font-family:"Montserrat",Arial,sans-serif}
.btn{display:inline-block;border-radius:30px;font-size:15px;font-weight:600;letter-spacing:.5px;text-transform:uppercase;text-decoration:none;text-align:center}
.btn-teal{background:var(--teal-dark);color:var(--white);padding:14px 30px}
.btn-navy{background:var(--blue);color:var(--white);padding:12px 28px}
.btn-outline{border:2px solid var(--blue);color:var(--blue);padding:10px 28px;background:var(--white)}

/* hero */
.hero{position:absolute;left:0;top:0;width:1200px;height:680px;overflow:hidden}
.hero-photo{position:absolute;inset:0;background:linear-gradient(100deg,#f4f6f8 0%,#e9edf0 40%,#c9d3db 65%,#9fb0bd 100%)}
.header{position:absolute;left:0;top:0;width:1200px;height:100px;display:flex;align-items:center;justify-content:space-between;padding:0 170px}
.brand{display:flex;align-items:center;gap:12px;font-size:26px;font-weight:800;color:var(--navy);letter-spacing:.5px}
.brand-mark{width:40px;height:40px;background:var(--teal)}
.nav{display:flex;align-items:center;gap:38px}
.nav a{font-size:15px;font-weight:600;color:var(--navy);text-decoration:none}
.nav .btn-navy{padding:10px 30px;color:var(--white)}
.hero-copy{position:absolute;left:170px;top:140px}
.hero-copy h1{font-size:48px;font-weight:800;color:var(--teal-dark);letter-spacing:.5px}
.hero-copy h1 span{color:var(--navy)}
.hero-copy p{margin-top:16px;font-family:"Montserrat",sans-serif;font-size:28px;line-height:38px;color:var(--navy);font-weight:500}
.hero-copy .btn{margin-top:34px}
.dots{position:absolute;left:580px;top:632px;display:flex;gap:10px}
.dots i{width:13px;height:13px;border-radius:50%;border:2px solid var(--blue);display:block}
.dots i.on{background:var(--teal)}

/* section titles */
.section-title{text-align:center;font-size:34px;font-weight:700;color:var(--navy);letter-spacing:.5px}
.section-title span{color:var(--teal-dark)}
.section-title::after{content:"";display:block;width:60px;height:3px;background:var(--teal);margin:14px auto 0}

.about{position:absolute;left:0;top:680px;width:1200px;height:360px;text-align:center;padding-top:80px}
.about p{width:860px;margin:34px auto 0;font-size:13px;line-height:22px;color:#555}
.about .btn{margin-top:34px}

.features{position:absolute;left:0;top:1048px;width:1200px;height:292px;background:var(--grey)}
.feature{position:absolute;top:82px;width:290px;height:210px;background:var(--white);text-align:center;padding:40px 34px 0}
.feature p{font-size:13px;line-height:20px;color:var(--muted);margin-top:20px}
.feature.active{background:var(--blue);height:230px;top:82px}
.feature.active p{color:#d8e4f2}
.feature .more{position:absolute;left:126px;bottom:-18px;width:38px;height:38px;border-radius:50%;background:var(--navy);border:3px solid var(--white)}

.pricing{position:absolute;left:0;top:1340px;width:1200px;height:650px;padding-top:42px}
.plan{position:absolute;top:1440px;width:272px;height:490px;background:var(--white);box-shadow:0 6px 22px rgba(10,63,126,.18);text-align:center}
.plan-head{height:92px;background:linear-gradient(180deg,var(--teal-dark),var(--mid));clip-path:polygon(0 0,100% 0,100% 78%,50% 100%,0 78%);color:var(--white);font-family:"Montserrat",sans-serif;font-weight:700;font-size:17px;line-height:22px;padding-top:22px}
.price{font-family:"Montserrat",sans-serif;font-weight:700;font-size:48px;color:var(--navy);margin-top:24px}
.price sup{font-size:20px;vertical-align:26px}
.plan ul{list-style:none;width:200px;margin:22px auto 0}
.plan li{font-size:15px;color:#666;padding:16px 0;border-top:1px solid #dde1e5}
.plan li:first-child{border-top:1px solid #dde1e5}
.plan .btn{position:absolute;left:50%;transform:translateX(-50%);bottom:50px;font-size:13px;padding:12px 24px;white-space:nowrap}

.blog{position:absolute;left:0;top:1990px;width:1200px;height:560px;background:var(--grey);padding-top:80px}
.post{position:absolute;top:2146px;width:272px}
.post-photo{height:216px}
.post h3{font-family:"Open Sans",sans-serif;font-weight:600;font-size:19px;line-height:25px;color:var(--ink);margin-top:22px}
.meta{display:flex;gap:20px;margin-top:14px;font-size:11px;color:var(--muted)}
.meta b{display:inline-block;width:8px;height:8px;background:var(--light);margin-right:6px;border-radius:2px}

.cta{position:absolute;left:0;top:2550px;width:1200px;height:190px;background:linear-gradient(90deg,#0a2f63,#123f7c 50%,#0a2f63);text-align:center;padding-top:28px}
.cta p{color:var(--white);font-family:"Montserrat",sans-serif;font-size:28px;line-height:36px;font-weight:500}
.cta .btn{margin-top:16px;padding:10px 34px;font-size:14px}

.footer{position:absolute;left:0;top:2740px;width:1200px;height:204px;display:flex;align-items:center;justify-content:space-between;padding:0 170px}
.footer .nav{gap:30px}
.footer .nav a{font-size:14px;color:var(--navy)}
.copy{font-size:11px;color:var(--muted);text-align:center;margin-top:10px}
.social{display:flex;gap:10px}
.social i{width:28px;height:28px;border-radius:50%;background:var(--mid);display:block}
</style>
</head>
<body>

<section class="hero">
  <div class="hero-photo" role="img" aria-label="Bright office desk with a monitor showing investment charts"></div>
  <header class="header">
    <div class="brand"><span class="brand-mark"></span>yieldcompassPlans</div>
    <nav class="nav">
      <a href="#">ABOUT</a><a href="#">PRICING</a><a href="#">BLOG</a><a href="#">CONTACT</a>
      <a class="btn btn-navy" href="#">LOG IN</a>
    </nav>
  </header>
  <div class="hero-copy">
    <h1><span>WIN MORE,</span> LOSE LESS</h1>
    <p>Investment strategies<br>that boost returns and limit risk.</p>
    <a class="btn btn-teal" href="#">SIGN UP FREE</a>
  </div>
  <div class="dots"><i></i><i class="on"></i><i></i></div>
</section>

<section class="about">
  <h2 class="section-title">ABOUT <span>YIELDCOMPASSPLANS</span></h2>
  <p>Our members receive systematic, rules-based investment strategies every month, built from transparent signals and tested over many market cycles. Each model portfolio is designed to capture growth while limiting deep losses, so individual investors can follow a clear plan instead of guessing. Review the current allocations, compare performance charts, and adjust your own holdings with confidence and discipline.</p>
  <a class="btn btn-outline" href="#">READ MORE</a>
</section>

<section class="features">
  <div class="feature" style="left:170px">
    <svg width="34" height="34" viewBox="0 0 34 34" fill="none" stroke="#0355a3" stroke-width="2"><circle cx="17" cy="17" r="14"/><path d="M3 17h28M17 3c5 5 5 23 0 28M17 3c-5 5-5 23 0 28"/></svg>
    <p>When you can't afford to lose, our model portfolios help protect investments by reducing holdings to risky assets when the market turns down.</p>
  </div>
  <div class="feature active" style="left:455px">
    <svg width="34" height="34" viewBox="0 0 34 34" fill="none" stroke="#ffffff" stroke-width="2"><circle cx="17" cy="17" r="14"/><path d="M10 22l6-6 4 4 6-8"/></svg>
    <p>Our dynamic portfolios find the best places to invest. They adjust monthly to invest in the strongest funds.</p>
    <span class="more"></span>
  </div>
  <div class="feature" style="left:740px">
    <svg width="34" height="34" viewBox="0 0 34 34" fill="none" stroke="#0355a3" stroke-width="2"><rect x="4" y="8" width="26" height="18" rx="2"/><path d="M4 10l13 9 13-9"/></svg>
    <p>You receive monthly email recommendations, generated from our systematic, rules-based models.</p>
  </div>
</section>

<section class="pricing">
  <h2 class="section-title">OUR PRICING</h2>
</section>
<div class="plan" style="left:160px">
  <div class="plan-head">LIMITED FREE<br>MEMBERSHIP</div>
  <div class="price">FREE</div>
  <ul><li>Basic Strategies</li><li>Trends Tracker</li></ul>
  <a class="btn btn-navy" href="#">FREE MEMBERSHIP</a>
</div>
<div class="plan" style="left:464px">
  <div class="plan-head">MONTHLY<br>MEMBERSHIP</div>
  <div class="price"><sup>$</sup>19<sup>95</sup></div>
  <ul><li>Basic Strategies</li><li>Advanced Strategies</li><li>Trends Tracker</li></ul>
  <a class="btn btn-navy" href="#">MONTHLY MEMBERSHIP</a>
</div>
<div class="plan" style="left:768px">
  <div class="plan-head">ANNUAL<br>MEMBERSHIP</div>
  <div class="price"><sup>$</sup>149<sup>95</sup></div>
  <ul><li>Basic Strategies</li><li>Advanced Strategies</li><li>Trends Tracker</li></ul>
  <a class="btn btn-navy" href="#">ANNUAL MEMBERSHIP</a>
</div>

<section class="blog">
  <h2 class="section-title">LATEST BLOG</h2>
</section>
<article class="post" style="left:160px">
  <div class="post-photo" role="img" aria-label="Hands holding a phone above a desk with financial papers" style="background:linear-gradient(135deg,#c9b9a5,#8c7c6c 60%,#5a4f47)"></div>
  <h3>At vero eos et accusamus et iusto odio dignissi</h3>
  <div class="meta"><span><b></b>05/12/2018</span><span><b></b>Sam Ortel</span></div>
</article>
<article class="post" style="left:464px">
  <div class="post-photo" role="img" aria-label="Team reviewing printed charts around a table" style="background:linear-gradient(135deg,#aeb7c0,#6f7f8f 55%,#3d4c5b)"></div>
  <h3>At vero eos et accusamus et iusto odio dignissi</h3>
  <div class="meta"><span><b></b>05/12/2018</span><span><b></b>Sam Ortel</span></div>
</article>
<article class="post" style="left:768px">
  <div class="post-photo" role="img" aria-label="Desk covered with financial reports and graphs" style="background:linear-gradient(135deg,#e4e8ea,#b7c3cb 55%,#7d8f9c)"></div>
  <h3>At vero eos et accusamus et iusto odio dignissi</h3>
  <div class="meta"><span><b></b>05/12/2018</span><span><b></b>Sam Ortel</span></div>
</article>

<section class="cta" role="img" aria-label="Dark blue background of city financial district">
  <p>Worried about recent stock market volatility?<br>Learn how our momentum strategies can protect against loses.</p>
  <a class="btn btn-teal" href="#">FREE SIGN UP</a>
</section>

<footer class="footer">
  <div class="brand"><span class="brand-mark"></span>yieldcompassPlans</div>
  <div>
    <nav class="nav"><a href="#">ABOUT</a><a href="#">PRICING</a><a href="#">BLOG</a><a href="#">CONTACT</a></nav>
    <div class="copy">© 2018 Company Name. All rights reserved.</div>
  </div>
  <div class="social"><i></i><i></i><i></i><i></i></div>
</footer>

</body>
</html>
```